Real Estate Seller Financing Postcard

I need a postcard that lays out these options contained in the notes that grabs attention, explains the two options easily and is eye-catching. The front needs to have the percentages on it and information about it and on the other side One side exact Text is:
"Monthly income without tenant headaches" in big letters. Also on front "Get
110%
add an "or"
160% of market value for your property. ". The percentages should be displayed and that is not to be a sentence of text. Other side text: I need bullets points for these "Formal protection as a lien holder against home
No commission or closing cost
Fast closings possible
Property taken as is so no repairs.

Add to the top of the back in "It’s simple. I am a new investor without down payment capital who still want to double our portfolio this year to grow our portfolio."
Here are the two options that are to be the largest part of the back
Option 1, you can receive 80% now cash and 30% over a short period of time including interest.

Option 2, where act like a bank allowing you to make 150% if you finance the whole property(ies). No gimmicks and surprises, just simple unconventional financing.

Include Logo Somewhere

Target Market(s)

Property Owners Wanting to Sell Their Property

Industry/Entity Type

Real Estate Investing

Requirements
Must have
• The options promiment and each side with its respective information. Must have logo somewhere
Nice to have
• The options in color other than black.
Should not have
• A picture of money on the front. Any other image is okay.

```html
<!DOCTYPE html>
<html lang="en">
<head>
<meta charset="UTF-8">
<title>Meridian Real Estate Group – Seller Financing Postcard</title>
<link rel="stylesheet" href="https://fonts.googleapis.com/css2?family=Montserrat:ital,wght@0,300;0,400;0,500;0,600;0,700;1,700&display=swap">
<style>
  :root {
    --stage: #e6e7e9;
    --navy-deep: #03061a;
    --navy: #0b2a78;
    --royal: #1a4aa8;
    --glow: #4fb2f0;
    --brand-blue: #1f4aa3;
    --band-start: #0c2f80;
    --band-end: #1b4fae;
    --slate: #8a8d92;
    --ink: #1a1a1a;
    --white: #ffffff;
  }
  * { box-sizing: border-box; margin: 0; padding: 0; }
  html, body {
    width: 1108px; height: 1200px; overflow: hidden;
    background: var(--stage);
    font-family: "Montserrat", Arial, sans-serif;
  }
  .card {
    position: absolute;
    width: 820px; height: 540px;
    overflow: hidden;
    box-shadow: 0 6px 18px rgba(0,0,0,.25);
  }

  /* ---------- Front ---------- */
  .card--front {
    left: 60px; top: 40px;
    background:
      radial-gradient(ellipse 380px 260px at 420px 470px, rgba(79,178,240,.85), rgba(26,74,168,.55) 45%, transparent 80%),
      radial-gradient(ellipse 520px 380px at 260px 320px, var(--royal), transparent 75%),
      linear-gradient(160deg, var(--navy-deep) 0%, #061449 45%, var(--navy) 100%);
    color: var(--white);
  }
  .front-copy { position: absolute; left: 64px; top: 88px; width: 320px; text-align: center; }
  .front-lead { font-size: 23px; font-weight: 300; text-align: left; }
  .front-lead strong { font-weight: 600; }
  .front-figure { font-size: 118px; font-weight: 300; line-height: 1; letter-spacing: -3px; text-align: left; }
  .front-or { font-size: 22px; font-weight: 700; margin: 26px 0 30px; }
  .front-tail { font-size: 27px; font-weight: 300; line-height: 1.05; margin-top: 4px; }
  .front-tail strong { font-weight: 600; }
  .front-art {
    position: absolute; left: 380px; top: 90px; width: 420px; height: 380px;
    background: radial-gradient(ellipse 150px 170px at 250px 180px, rgba(235,238,242,.95), rgba(170,185,205,.6) 60%, transparent 100%);
  }
  .brand {
    display: flex; align-items: center; gap: 10px;
  }
  .brand-dot { border-radius: 50%; border: 2px solid var(--brand-blue); flex: none; }
  .brand-name { font-weight: 500; color: var(--brand-blue); line-height: 1.1; }
  .card--front .brand { position: absolute; right: 58px; bottom: 52px; }
  .card--front .brand-dot { width: 42px; height: 42px; border-color: var(--glow); }
  .card--front .brand-name { font-size: 16px; color: var(--glow); }

  /* ---------- Back ---------- */
  .card--back { left: 228px; top: 620px; background: var(--white); }
  .card--back .brand { position: absolute; left: 220px; top: 40px; }
  .card--back .brand-dot { width: 90px; height: 90px; border-width: 3px; }
  .card--back .brand-name { font-size: 28px; }
  .back-quote {
    position: absolute; left: 70px; top: 170px; width: 690px;
    font-size: 17px; color: var(--ink); line-height: 1.2; text-align: center;
  }
  .back-quote strong { font-weight: 700; }
  .benefits {
    position: absolute; left: 90px; top: 270px; width: 270px;
    list-style: none; color: var(--brand-blue); font-weight: 500; font-size: 17px; line-height: 1.45;
  }
  .benefits li { position: relative; padding-left: 26px; margin-bottom: 4px; }
  .benefits li::before {
    content: ""; position: absolute; left: 2px; top: 10px;
    width: 7px; height: 7px; border-radius: 50%; background: var(--brand-blue);
  }
  .options { position: absolute; left: 370px; top: 256px; width: 450px; }
  .option { display: flex; height: 94px; margin-bottom: 14px; }
  .option-num {
    width: 100px; background: var(--slate); color: var(--white);
    display: flex; flex-direction: column; justify-content: center; padding-left: 14px;
  }
  .option-label { font-size: 15px; font-weight: 600; letter-spacing: .5px; }
  .option-digits { font-size: 54px; font-weight: 300; line-height: 1; }
  .option-text {
    flex: 1; background: linear-gradient(90deg, var(--band-start), var(--band-end));
    color: var(--white); font-size: 18px; font-weight: 400; line-height: 1.2;
    padding: 12px 20px; display: flex; align-items: center;
  }
  .option-text strong { font-weight: 700; }
  .back-tagline {
    position: absolute; left: 0; right: 0; bottom: 40px; text-align: center;
    color: var(--brand-blue); font-size: 19px; font-weight: 700; font-style: italic;
  }
</style>
</head>
<body>

<section class="card card--front">
  <div class="front-copy">
    <p class="front-lead">Have the <strong>ability to make</strong></p>
    <p class="front-figure">110%</p>
    <p class="front-or">OR</p>
    <p class="front-figure">160%</p>
    <p class="front-tail"><strong>market value</strong> for your<br>property.</p>
  </div>
  <div class="front-art" role="img" aria-label="Illustration of a white house-shaped archery target with an arrow in the blue bullseye"></div>
  <div class="brand">
    <span class="brand-dot"></span>
    <span class="brand-name">MERIDIAN<br>REAL ESTATE GROUP</span>
  </div>
</section>

<section class="card card--back">
  <div class="brand">
    <span class="brand-dot"></span>
    <span class="brand-name">MERIDIAN<br>REAL ESTATE GROUP</span>
  </div>
  <p class="back-quote">“<strong>It’s simple.</strong> I am a new investor without down payment capital who still would like to double our portfolio this year to grow our portfolio.”</p>
  <ul class="benefits">
    <li>Formal protection as a lien holder against home.</li>
    <li>No commission or closing cost.</li>
    <li>Fast closings possible.</li>
    <li>Property taken as is so no repairs.</li>
  </ul>
  <div class="options">
    <div class="option">
      <div class="option-num"><span class="option-label">OPTION</span><span class="option-digits">01</span></div>
      <p class="option-text"><span>Receive <strong>80% cash now</strong> and <strong>30%</strong> over a short period of time including interest.</span></p>
    </div>
    <div class="option">
      <div class="option-num"><span class="option-label">OPTION</span><span class="option-digits">02</span></div>
      <p class="option-text"><span>We act like a bank allowing you to <strong>make 150%</strong> if you finance the whole property(ies).</span></p>
    </div>
  </div>
  <p class="back-tagline">No gimmicks and surprises, just simple unconventional financing.</p>
</section>

</body>
</html>
```